Fall Convention Graphic Designs (logo, digital brochure, t-shirt designs, social media templates)

I need a graphic package for the Brightwell Dance Guild Fall Dance Convention. Brightwell Dance Guild is a non-profit organization of dance teachers, and this educational dance conference is for members and their students with multiple events throughout the weekend. The convention has a new them each year. I will need a package with a general "logo" type graphic, a digital brochure, t-shirt design, and social media graphic templates. This year's Convention has a general theme and names for each event throughout the weekend.
The theme and event names for this year are:
Convention Theme Tales in Motion: Beneath a Silver Sky
Registration Desk The Willow Nook
Members Welcome A Golden Greeting
Banquet A Velvet Soiree
President's Reception Glow Beyond Dusk
Jr. Member Desk Wanderers' Wharf
Jr. Member Pizza Party Meadow Mixer
Members Luncheon Harbor Reveries

I am attaching a word file that includes information and text to be included in brochure. Also attached are designs from previous years for brochures, T-shirts, and social media graphics.

Colors that we will be using for decorations at various events over the weekend this year are shades of green (fern and mossy green), shades of blue (including navy), white, and pinks (including mauve). The banquet event will be decorated as an enchanted forest. We are using fairy lights, books that look like a storybook, and lanterns for decorations as well. I think I would like a more modern design, and I do not want anything that is childish or too whimsical. While we are using floral decorations I don't want bunches of flowers in the design.

*I am open to seeing initial logo type designs and giving feedback to make sure it is a direction that I like and then moving forward with the other parts of the project.

```html
<!DOCTYPE html>
<html lang="en">
<head>
<meta charset="utf-8">
<title>Brightwell Dance Guild Fall Convention Brochure</title>
<link href="https://fonts.googleapis.com/css2?family=Cinzel:wght@400;600&family=Fira+Sans:wght@300;400;600&display=swap" rel="stylesheet">
<style>
  :root{
    --backdrop:#3b3b3b;
    --navy-deep:#081223;
    --navy:#14284a;
    --navy-mid:#203a5e;
    --text:#eef1f6;
    --muted:#cfd6e2;
    --mauve:#b98a99;
    --mauve-tab:#b58693;
    --fern:#4f6a4b;
    --lantern-red:#c8341f;
    --gold:#8a7440;
  }
  *{margin:0;padding:0;box-sizing:border-box}
  html,body{width:1200px;height:4190px;overflow:hidden;background:var(--backdrop)}
  body{position:relative;font-family:"Fira Sans",sans-serif;color:var(--text)}
  .page{position:absolute;left:141px;width:918px;height:1186px;overflow:hidden}
  .page--cover{top:177px}
  .page--schedule{top:1501px}
  .page--info{top:2824px}
  .forest-bg{position:absolute;inset:0;
    background:radial-gradient(ellipse at 45% 30%,var(--navy-mid) 0%,var(--navy) 45%,var(--navy-deep) 100%)}
  .lantern-art{position:absolute;top:0;right:40px;width:161px;height:221px;
    background:radial-gradient(ellipse at 45% 40%,#e04a2a 0%,var(--lantern-red) 40%,rgba(120,30,20,0) 72%)}
  .page--schedule .lantern-art,.page--info .lantern-art{right:0;width:122px;height:150px;top:0}
  .lantern-border{position:absolute;left:0;right:0;bottom:0;height:176px;
    background:linear-gradient(to bottom,rgba(138,116,64,0) 0%,rgba(138,116,64,.18) 60%,rgba(138,116,64,.28) 100%)}
  .content{position:absolute;inset:0}
  .cover-title{position:absolute;top:90px;left:0;right:0;text-align:center;
    font-family:"Cinzel",serif;font-size:68px;line-height:86px;font-weight:400;letter-spacing:1px}
  .cover-details{position:absolute;top:475px;left:0;right:0;text-align:center;
    font-weight:300;font-size:26px;line-height:45.5px}
  .cover-details .gap{height:45.5px}
  .room-link{position:absolute;top:1064px;left:0;right:0;text-align:center;font-size:18px;font-weight:300;color:var(--mauve)}
  .org-name{position:absolute;top:40px;left:0;right:0;text-align:center;font-family:"Cinzel",serif;font-size:25px}
  .event-title{position:absolute;top:70px;left:0;right:0;text-align:center;font-family:"Cinzel",serif;font-size:70px;line-height:80px}
  .ribbon{position:absolute;left:260px;width:397px;height:41px;background:var(--fern);
    clip-path:polygon(4% 0,96% 0,100% 50%,96% 100%,4% 100%,0 50%);
    display:flex;align-items:center;justify-content:center}
  .ribbon--theme{top:153px;font-size:15.5px;color:#dfe4da;font-weight:300}
  .ribbon--section{font-family:"Cinzel",serif;font-size:21px;color:var(--text)}
  .theme-tab{position:absolute;left:166px;top:215px;width:42px;height:283px;background:var(--mauve-tab);
    display:flex;align-items:center;justify-content:center}
  .theme-tab span{transform:rotate(-90deg);white-space:nowrap;font-family:"Cinzel",serif;font-size:11px;color:#f3e9ec}
  .theme-table{position:absolute;left:215px;top:215px;width:536px;height:283px;border:1px solid #b8c2d2;border-collapse:collapse;font-size:11px}
  .theme-table th{background:#fff;color:var(--mauve);font-family:"Cinzel",serif;font-weight:400;text-align:left;height:35px;font-size:12px}
  .theme-table td{height:29.6px;color:var(--text)}
  .theme-table .col-event{padding-left:50px;width:240px}
  .schedule{position:absolute;left:130px;right:60px}
  .day{font-family:"Cinzel",serif;font-weight:600;font-size:21px;margin-bottom:8px}
  .day-items{font-size:12px;line-height:24px;font-weight:300}
  .day-sub{font-size:12px;font-weight:400;margin-top:-6px;margin-bottom:10px}
  .timetable td{font-size:12px;font-weight:300;height:24.2px;padding:0;vertical-align:middle}
  .timetable .t{width:117px}
  .timetable .n{width:142px}
  .info{position:absolute;top:141px;left:94px;width:729px;font-size:13.5px;line-height:26px;font-weight:300;text-align:justify}
  .info p{margin-bottom:26px}
  .info p.tight{margin-bottom:0}
  .featured{font-weight:600;font-size:20px;color:var(--mauve);margin-top:0;line-height:30px}
  .faculty{list-style:none;margin-top:24px;font-size:20px;line-height:34px;font-weight:300}
</style>
</head>
<body>

<section class="page page--cover">
  <div class="forest-bg" role="img" aria-label="Night forest photograph in deep navy blue with falling sparkles"></div>
  <div class="lantern-art" role="img" aria-label="Two hanging red paper lanterns with gold tassels"></div>
  <div class="lantern-border" role="img" aria-label="Row of gold line-art lanterns along the bottom edge"></div>
  <div class="content">
    <h1 class="cover-title">Brightwell<br>Dance Guild<br>Fall<br>Convention</h1>
    <div class="cover-details">
      <p>November 19 – 22, 2026</p>
      <p>Ashcombe Convention Center</p>
      <p>Halden Grand Hotel</p>
      <p>Greensboro, NC</p>
      <div class="gap"></div>
      <p>Teacher’s Intensive on Friday</p>
      <div class="gap"></div>
      <p>Outstanding accommodations at the</p>
      <p>Halden Grand Hotel</p>
      <p>4580 Linden Park Avenue, Greensboro, NC 27499</p>
      <p>Call for reservations and mention BDG for your best rate!</p>
      <p>336-555-0148 or book online.</p>
    </div>
    <p class="room-link">[Insert Link for Room Block]</p>
  </div>
</section>

<section class="page page--schedule">
  <div class="forest-bg" role="img" aria-label="Night forest photograph in deep navy blue with falling sparkles"></div>
  <div class="lantern-art" role="img" aria-label="Hanging red paper lanterns in the corner"></div>
  <div class="content">
    <p class="org-name">BRIGHTWELL DANCE GUILD, INC.</p>
    <h2 class="event-title">FALL CONVENTION</h2>
    <div class="ribbon ribbon--theme">Tales in Motion: Beneath a Silver Sky</div>
    <div class="theme-tab"><span>CONVENTION THEME &amp; EVENT NAMES</span></div>
    <table class="theme-table">
      <tr><th class="col-event">EVENT</th><th>NAME</th></tr>
      <tr><td class="col-event">Convention Theme</td><td>Tales in Motion: Beneath a Silver Sky</td></tr>
      <tr><td class="col-event">Registration Desk</td><td>The Willow Nook</td></tr>
      <tr><td class="col-event">Members Welcome</td><td>A Golden Greeting</td></tr>
      <tr><td class="col-event">Banquet</td><td>A Velvet Soiree</td></tr>
      <tr><td class="col-event">President’s Reception</td><td>Glow Beyond Dusk</td></tr>
      <tr><td class="col-event">Jr. Member Desk</td><td>Wanderers’ Wharf</td></tr>
      <tr><td class="col-event">Jr. Member Pizza Party</td><td>Meadow Mixer</td></tr>
      <tr><td class="col-event">Members Luncheon</td><td>Harbor Reveries</td></tr>
    </table>
    <div class="ribbon ribbon--section" style="top:541px">SCHEDULE OF EVENTS</div>

    <div class="schedule" style="top:608px">
      <h3 class="day">THURSDAY, NOVEMBER 19TH</h3>
      <div class="day-items">
        <p>Solo Title Scholarship Competition Audition Classes, Interviews, and Opening Number Rehearsals</p>
        <p>A Golden Greeting– Members Welcome Party</p>
      </div>
    </div>
    <div class="schedule" style="top:713px">
      <h3 class="day">FRIDAY, NOVEMBER 20TH</h3>
      <div class="day-items">
        <p>Teachers Intensive</p>
        <p>Solo Title Scholarship Competition Audition Classes, Interviews, and Opening Number Rehearsals</p>
        <p>Registration Packet Pickup</p>
        <p>Solo Title Scholarship Competition and Crowning</p>
        <p>Meadow Mixer - Jr. Members Pizza and Pajama Party</p>
      </div>
    </div>
    <div class="schedule" style="top:891px">
      <h3 class="day">SATURDAY, NOVEMBER 21ST</h3>
      <p class="day-sub">Halden Grand Hotel, Ashcombe Convention Center</p>
      <table class="timetable">
        <tr><td class="t">8:00am</td><td class="n">The Willow Nook</td><td>Registration Desk Opens</td></tr>
        <tr><td class="t">8:00am</td><td class="n">Wanderers’ Wharf</td><td>Junior Member Desk Opens</td></tr>
        <tr><td class="t">8:00am-8:45am</td><td colspan="2">Junior Member Banquet Performance Rehearsal</td></tr>
        <tr><td class="t">9:00am-1:00pm</td><td class="n">Convention Classes</td><td>Mini</td></tr>
        <tr><td class="t">9:00am-3:00pm</td><td class="n">Convention Classes</td><td>Junior | Senior | Teachers &amp; Assistants</td></tr>
        <tr><td class="t">6:00pm-7:30pm</td><td colspan="2">Banquet – A Velvet Soiree</td></tr>
        <tr><td class="t">8:30pm</td><td colspan="2">Miss and Mr. Talent and Crowning</td></tr>
        <tr><td class="t">10:00pm</td><td colspan="2">Glow Beyond Dusk - President’s Reception (Immediately following Miss / Mr. Dance Crowning)</td></tr>
      </table>
    </div>
  </div>
</section>

<section class="page page--info">
  <div class="forest-bg" role="img" aria-label="Night forest photograph in deep navy blue with falling sparkles"></div>
  <div class="lantern-art" role="img" aria-label="Hanging red paper lanterns in the corner"></div>
  <div class="lantern-border" role="img" aria-label="Row of gold line-art lanterns along the bottom edge"></div>
  <div class="content">
    <div class="ribbon ribbon--section" style="top:57px">VALUABLE INFORMATION</div>
    <div class="info">
      <p>Classroom Attire: Students &amp; teachers should be dressed in proper dance attire; leotards, tights and appropriate dance shoes. Cover ups must be worn at all times when leaving class and walking through the hotel. Tap shoes are not allowed outside of the classroom. No bare midriffs please.</p>
      <p>One badge for a parent/monitor will be given to each studio that registers Mini &amp; Junior students (one for each classroom). These people, designated by your studio, will be responsible for your Mini &amp; Junior students concerning bathroom, changing shoes, conduct, etc.</p>
      <p>Banquet Attire: Semi-formal or formal attire for students, formal attire for teachers and parents.</p>
      <p>Recommended Ages: Mini 6-3, Junior 9-13, Senior 14 &amp; up, Advanced is intended for teaching professionals.</p>
      <p class="tight">Pageant program books, banquet tickets and t-shirts must be pre-ordered.</p>
      <p>**T-shirts are NOT included with Registration and must be preordered ($25). A very limited number will be available on site**</p>
      <p>Contestants in Solo Title Scholarship Competition are required to attend all classes in their age level.</p>
      <p>All members’ dues must have been post-marked by September 1, 2026 to receive the member rate, You must also pre-register for the Members Luncheon on Sunday.</p>
      <p>Video recording of classes will be allowed. Video recording and photos during pageant IS NOT ALLOWED.</p>
      <p>FACULTY *I will need to be able to add in headshots for each of these people when I get them. Please leave a place holder</p>
      <p>Teachers Intensive – Featured Guest and underneath Friday November 20th</p>
      <p class="featured">MARISOL VANTREE</p>
      <ul class="faculty">
        <li>Corinne Ashby</li>
        <li>Tessa Fairlow</li>
        <li>Juliet Marlowe Pace</li>
        <li>Declan Rourke</li>
        <li>To Be Determined #1</li>
      </ul>
    </div>
  </div>
</section>

</body>
</html>
```